Uregent Care opening postcard with coupon

We need a postcard created to mail directly to homes. The flyer need to be appealing and include a small spot with a coupon for $20 gift card with first visit. The post card needs to be 2 sided and 4X6. We have a logo. To learn more about us visit maplegroveclinicplus.example or check us out on facebook. I will try to figure out how to upload logo.

Target Market(s)

All households that need urgent care.

Industry/Entity Type

Healthcare

Font styles to use
Serif

Colors
33a6d7
447fba
85acd3
85cae6
cfdfed
ecf7fb

Requirements
Must have
• our logo
• family centered
• some services offered
• coupon with free $20 gc at first visit if you bring in this flyer
Nice to have
• visually appealing

```html
<!DOCTYPE html>
<html lang="en">
<head>
<meta charset="utf-8">
<title>Maple Grove Clinic Plus – Postcard</title>
<link rel="stylesheet" href="https://fonts.googleapis.com/css2?family=Roboto+Condensed:wght@700&family=Hind:wght@500;600&family=Nunito:wght@600;700&display=swap">
<style>
  :root {
    --backdrop: #231f20;
    --brand-blue: #4270b6;
    --brand-navy: #1b1a4e;
    --paper: #ffffff;
    --silver-dark: #c9cacc;
    --silver-light: #f4f4f5;
    --photo-a: #e8ebf0;
    --photo-b: #c6cfdc;
  }
  * { box-sizing: border-box; margin: 0; padding: 0; }
  html, body { width: 800px; height: 1200px; overflow: hidden; background: var(--backdrop); }
  .canvas { position: relative; width: 800px; height: 1200px; }

  .card { position: absolute; left: 66px; width: 669px; overflow: hidden; background: var(--paper); }
  .card--front { top: 70px; height: 516px; }
  .card--back { top: 614px; height: 514px; }

  /* Front */
  .front-header { position: absolute; left: 0; top: 0; width: 100%; height: 141px;
    background: linear-gradient(90deg, var(--silver-dark) 0%, var(--silver-light) 28%, var(--paper) 45%); }
  .brand { position: absolute; display: flex; align-items: center; font-family: "Roboto Condensed", sans-serif; font-weight: 700; color: var(--brand-navy); }
  .brand__mark { background: var(--brand-navy); flex: none; }
  .brand__name { line-height: 0.95; }
  .brand__name span { display: block; }
  .brand--front { left: 80px; top: 20px; gap: 26px; }
  .brand--front .brand__mark { width: 84px; height: 84px; }
  .brand--front .brand__name { font-size: 48px; }
  .brand--front .brand__name span:last-child { font-size: 54px; }

  .front-rule { position: absolute; left: 0; top: 141px; width: 100%; height: 9px; background: var(--brand-blue); }
  .front-body { position: absolute; left: 0; top: 150px; width: 100%; height: 366px;
    background: linear-gradient(90deg, var(--silver-dark) 0%, var(--silver-light) 30%, var(--paper) 55%); }
  .family-photo { position: absolute; right: 0; top: 154px; width: 390px; height: 362px;
    background: radial-gradient(ellipse at 55% 55%, var(--photo-b) 0%, var(--photo-a) 60%, var(--paper) 100%); }

  .offer { position: absolute; left: 28px; top: 166px; font-family: "Roboto Condensed", sans-serif; font-weight: 700; color: var(--brand-blue); }
  .offer__amount { font-size: 210px; line-height: 1; letter-spacing: -8px; transform: scaleX(0.92); transform-origin: left; }
  .offer__note { position: absolute; left: 58px; top: 186px; font-size: 20px; white-space: nowrap; transform: scaleX(0.85); transform-origin: left; }

  .contact { position: absolute; left: 18px; top: 393px; width: 270px; text-align: center; font-family: "Hind", sans-serif; color: var(--brand-navy); }
  .contact__phone { font-size: 35px; font-weight: 600; line-height: 1.1; }
  .contact__address { font-size: 20px; font-weight: 500; line-height: 1.25; margin-top: 4px; }

  /* Back */
  .back-panel { position: absolute; left: 0; top: 0; width: 669px; height: 465px; }
  .services { position: absolute; left: 38px; top: 50px; width: 300px; font-family: "Nunito", sans-serif; color: var(--paper); }
  .services__title { font-size: 28px; font-weight: 700; letter-spacing: 0.3px; }
  .services__intro { font-size: 17px; font-weight: 600; line-height: 1.35; margin-top: 14px; }
  .services__list { list-style: none; margin-top: 14px; font-size: 13px; font-weight: 600; line-height: 16.3px; }
  .services__list li { position: relative; padding-left: 19px; }
  .services__list li::before { content: ""; position: absolute; left: 2px; top: 5px; width: 7px; height: 7px; border-radius: 50%; background: var(--paper); }
  .services__address { font-size: 20px; font-weight: 700; line-height: 1.3; margin-top: 11px; }

  .stamp-box { position: absolute; left: 547px; top: 47px; width: 91px; height: 91px; background: var(--brand-navy); }
  .brand--back { left: 342px; top: 220px; gap: 14px; }
  .brand--back .brand__mark { width: 56px; height: 56px; }
  .brand--back .brand__name { font-size: 32px; }
  .brand--back .brand__name span:last-child { font-size: 36px; }
  .address-line { position: absolute; left: 347px; width: 292px; height: 2px; background: var(--brand-navy); }

  .emergency-band { position: absolute; left: 0; top: 465px; width: 100%; height: 49px; background: var(--brand-navy);
    display: flex; align-items: center; justify-content: center; font-family: "Nunito", sans-serif; font-weight: 700; font-size: 21px; color: var(--paper); }
</style>
</head>
<body>
<main class="canvas">
  <section class="card card--front">
    <header class="front-header">
      <div class="brand brand--front">
        <span class="brand__mark"></span>
        <div class="brand__name"><span>Maple Grove</span><span>CLINIC PLUS</span></div>
      </div>
    </header>
    <div class="front-rule"></div>
    <div class="front-body"></div>
    <div class="family-photo" role="img" aria-label="Photo of a smiling family of four in white T-shirts and jeans"></div>
    <div class="offer">
      <div class="offer__amount">$20</div>
      <div class="offer__note">Gift card with first visit</div>
    </div>
    <div class="contact">
      <div class="contact__phone">(555) 014-2290</div>
      <div class="contact__address">1280 Harbor Lane Bayview,<br>Virginia 23500</div>
    </div>
  </section>

  <section class="card card--back">
    <svg class="back-panel" viewBox="0 0 669 465" aria-hidden="true">
      <polygon points="0,0 364,0 302,465 0,465" fill="var(--brand-blue)"/>
      <polygon points="364,0 373,0 311,465 302,465" fill="var(--brand-navy)"/>
    </svg>
    <div class="services">
      <h2 class="services__title">Services We Offer:</h2>
      <p class="services__intro">Offering a wide range of quick care patient services:</p>
      <ul class="services__list">
        <li>Urgent Care</li>
        <li>Flu Shots &amp; Vaccinations</li>
        <li>Sports &amp; Pre-Employment Physicals</li>
        <li>Mild/Moderate Illness and Injury Care</li>
        <li>On-Site Lab Testing &amp; X-Rays</li>
        <li>Personal Injury Care</li>
        <li>Sports Injury Care</li>
        <li>Minor MVA Injury Care</li>
        <li>STD Testing &amp; Treatment</li>
        <li>Tuberculosis Skin Tests</li>
        <li>Minor Ambulatory Procedures</li>
        <li>Drug Testing</li>
        <li>Pregnancy Test</li>
        <li>Medication Refills</li>
      </ul>
      <p class="services__address">1280 Harbor Lane<br>Bayview, Virginia 23500</p>
    </div>
    <div class="stamp-box"></div>
    <div class="brand brand--back">
      <span class="brand__mark"></span>
      <div class="brand__name"><span>Maple Grove</span><span>CLINIC PLUS</span></div>
    </div>
    <div class="address-line" style="top:358px"></div>
    <div class="address-line" style="top:394px"></div>
    <div class="address-line" style="top:430px"></div>
    <footer class="emergency-band">For Life-Threatening Emergencies Call 911</footer>
  </section>
</main>
</body>
</html>
```